Moss Lantern Sweets Business Card Design

Need a business card design for my eco-luxe dessert company Moss Lantern Sweets. The cards will be printed on 100% post consumer recycled content... so some kind of natural colored paper.

Two sided
Standard Size 2" x 3.5"

Front Content:
Logo
Local. Organic. Sustainable. (underneath logo)

Back Content:
Delia Hurst
Sustainable Pastry Chef
Fernbrook, Connecticut

www.mosslanternsweets.example
mosslanternsweets@mailbox.example
203-571-3064

QR Code (file image)

The cards are going to be printed on recycled paper similar to this color:
HEX: #D5BC84
RGB: 213/188/132

Target Market(s)

Eco-Conscious
Educated
Wealthy
Foodies

Industry/Entity Type

Business

Requirements
Must have
• Two sided Business Card
Standard Size 2" x 3.5"

Front Content:
Logo

Back Content:
Delia Hurst
Sustainable Pastry Chef
203-571-3064
www.mosslanternsweets.example
Fernbrook, Connecticut
*There will also be a QR code. When submitting designs please leave room for the code on the back and I will post the url for the code shortly.
Nice to have
• Earthy Colors (green, brown) with some vibrant oranges/gold

```html
<!DOCTYPE html>
<html lang="en">
<head>
<meta charset="utf-8">
<title>Moss Lantern Sweets – Business Card</title>
<link rel="stylesheet" href="https://fonts.googleapis.com/css2?family=PT+Serif&family=Arvo&family=Roboto+Condensed&display=swap">
<style>
  :root {
    --canvas: #ffffff;
    --front-green: #a5c93b;
    --back-light: #cfe02c;
    --back-mid: #4f9a24;
    --back-dark: #0e4318;
    --brand-brown: #4b2d2a;
    --brand-rule: #7a6a5a;
    --gold: #e8e04a;
    --contact-yellow: #e9ec3e;
    --divider: #1f3d14;
    --tagline: #1c1c1c;
  }
  * { margin: 0; padding: 0; box-sizing: border-box; }
  html, body { width: 1200px; height: 391px; overflow: hidden; background: var(--canvas); }
  .canvas { position: relative; width: 1200px; height: 391px; }

  .card { position: absolute; top: 34px; width: 548px; height: 315px; border-radius: 18px; overflow: hidden; }
  .card--front { left: 43px; background: var(--front-green); }
  .card--back {
    left: 609px;
    background:
      radial-gradient(ellipse at 10% 95%, var(--back-light) 0%, rgba(207,224,44,0) 55%),
      linear-gradient(115deg, var(--back-mid) 0%, #2f7a1e 45%, var(--back-dark) 100%);
  }

  .brand { position: absolute; text-align: center; }
  .brand__mark { display: block; margin: 0 auto; border-radius: 50%; background: var(--gold); }
  .brand__name { font-family: "PT Serif", serif; color: var(--brand-brown); white-space: nowrap; }
  .brand__rule { height: 1px; background: var(--brand-rule); }
  .brand__tagline { font-family: "PT Serif", serif; color: var(--tagline); white-space: nowrap; }

  .card--front .brand { left: 0; width: 548px; top: 98px; }
  .card--front .brand__mark { width: 46px; height: 46px; margin-bottom: 30px; }
  .card--front .brand__name { font-size: 30px; letter-spacing: 0.5px; line-height: 34px; }
  .card--front .brand__rule { width: 230px; margin: 8px auto 6px; }
  .card--front .brand__tagline { font-size: 17px; }

  .card--back .brand { left: 24px; width: 190px; top: 184px; }
  .card--back .brand__mark { width: 30px; height: 30px; margin-bottom: 22px; }
  .card--back .brand__name { font-size: 16px; line-height: 20px; }
  .card--back .brand__rule { width: 150px; margin: 5px auto 4px; }
  .card--back .brand__tagline { font-size: 11px; }

  .divider { position: absolute; left: 235px; top: 122px; width: 1.5px; height: 197px; background: var(--divider); }

  .contact { position: absolute; right: 34px; top: 124px; text-align: right; color: var(--contact-yellow); }
  .contact__name { font-family: "Arvo", serif; font-size: 15px; letter-spacing: 0.5px; }
  .contact__title { font-family: "Arvo", serif; font-size: 12.5px; margin-top: 8px; }
  .contact__list { list-style: none; margin-top: 30px; font-family: "Roboto Condensed", sans-serif; font-size: 14.5px; line-height: 18.5px; }
</style>
</head>
<body>
<main class="canvas">
  <section class="card card--front" aria-label="Card front">
    <div class="brand">
      <span class="brand__mark"></span>
      <p class="brand__name">MOSS LANTERN SWEETS</p>
      <div class="brand__rule"></div>
      <p class="brand__tagline">Local. Organic. Sustainable.</p>
    </div>
  </section>

  <section class="card card--back" aria-label="Card back">
    <div class="brand">
      <span class="brand__mark"></span>
      <p class="brand__name">MOSS LANTERN SWEETS</p>
      <div class="brand__rule"></div>
      <p class="brand__tagline">Local. Organic. Sustainable.</p>
    </div>
    <div class="divider"></div>
    <div class="contact">
      <p class="contact__name">Delia Hurst</p>
      <p class="contact__title">Sustainable Pastry Chef</p>
      <ul class="contact__list">
        <li>203-571-3064</li>
        <li>mosslanternsweets@mailbox.example</li>
        <li>www.mosslanternsweets.example</li>
        <li>Fernbrook, Connecticut</li>
        <li>QR Code (.................)</li>
      </ul>
    </div>
  </section>
</main>
</body>
</html>
```